Reef Glow

sunglasses, sihoullette of body, maybe wearing a bikini or sunglasses. I am offering spray tanning, body wraps, tanning beds, stand up, body art, airbrush makeup.

Target Market(s)

I would say my target is all ages, But tanning is a seasonal business and more beauty and aging concept. and around prom time I get my most profitable business. so 18 to 21 through march and april. then 25 to 55 through april to june.

Industry/Entity Type

Makeup

Contact Information for Business Card

Phone number: 701-238-5147 Owner: Jan Porvik (Lindqvast)

Colors

Designer to choose colors to be used in the design.

Requirements
Nice to have
• Sunglasses, silouttes of body wearing sunglasses or bikini, or picture of spray gun.

```html
<!DOCTYPE html>
<html lang="en">
<head>
<meta charset="utf-8">
<title>Reef Glow – Business Card</title>
<link rel="stylesheet" href="https://fonts.googleapis.com/css2?family=Marcellus&family=Yellowtail&family=Lato:wght@400&display=swap">
<style>
  :root {
    --backdrop: #2b2b2b;
    --card-teal: #1fbcb1;
    --sun-yellow: #f6ec1e;
    --pure-white: #ffffff;
    --divider: rgba(255, 255, 255, 0.85);
  }
  html, body {
    margin: 0;
    padding: 0;
    width: 1200px;
    height: 900px;
    overflow: hidden;
    background: var(--backdrop);
  }
  .canvas {
    position: relative;
    width: 1200px;
    height: 900px;
  }
  .card {
    position: absolute;
    left: 100px;
    top: 158px;
    width: 1000px;
    height: 584px;
    background: var(--card-teal);
    overflow: hidden;
  }
  .owner-first {
    position: absolute;
    left: 20px;
    top: 40px;
    margin: 0;
    font-family: "Yellowtail", cursive;
    font-weight: 400;
    font-size: 330px;
    line-height: 1;
    color: var(--sun-yellow);
    transform: rotate(-6deg);
    transform-origin: left top;
  }
  .brand-name {
    position: absolute;
    left: 250px;
    top: 250px;
    margin: 0;
    font-family: "Marcellus", serif;
    font-weight: 400;
    font-size: 56px;
    letter-spacing: 1px;
    line-height: 1;
    color: var(--pure-white);
    text-transform: uppercase;
    transform: rotate(-14deg);
    transform-origin: left center;
    white-space: nowrap;
  }
  .owner-last {
    position: absolute;
    left: 425px;
    top: 418px;
    margin: 0;
    font-family: "Yellowtail", cursive;
    font-size: 46px;
    line-height: 1;
    color: var(--sun-yellow);
    transform: rotate(-12deg);
    transform-origin: left center;
  }
  .phone {
    position: absolute;
    left: 452px;
    top: 478px;
    margin: 0;
    font-family: "Marcellus", serif;
    font-size: 26px;
    line-height: 1;
    color: var(--sun-yellow);
    transform: rotate(-12deg);
    transform-origin: left center;
    letter-spacing: 0.5px;
  }
  .divider {
    position: absolute;
    left: 752px;
    top: 79px;
    width: 2px;
    height: 420px;
    background: var(--divider);
  }
  .services {
    position: absolute;
    left: 793px;
    top: 212px;
    margin: 0;
    padding: 0;
    list-style: none;
    font-family: "Lato", sans-serif;
    font-size: 20px;
    line-height: 31px;
    color: var(--sun-yellow);
  }
  .services .initial {
    font-size: 26px;
  }
</style>
</head>
<body>
  <main class="canvas">
    <section class="card" aria-label="Reef Glow business card">
      <p class="owner-first">Jan</p>
      <h1 class="brand-name">Reef Glow</h1>
      <p class="owner-last">porvik</p>
      <p class="phone">701-238-5147</p>
      <div class="divider" aria-hidden="true"></div>
      <ul class="services">
        <li><span class="initial">S</span>pray tanning.</li>
        <li>Body wraps.</li>
        <li>Tanning beds.</li>
        <li>Stand up.</li>
        <li>Body art.</li>
        <li>Airbrush makeup.</li>
      </ul>
    </section>
  </main>
</body>
</html>
```